Fun and Flexible Word Template Design for Classroom Learning Resources

We're a global arts and education nonprofit based in New York. We're looking for a 2-page Word template design for our new collection of Learning Resources.
Page 1 of the template should include:
1. Lantern 9 logo (attached)
2. Resource title
3. Author photo
4. Author bio
5. Resource text
6. Sub-title text
7. Colored call-out box
Page 2 of the template should include:
2. Resource Title (in a smaller font)
3. Resource text
4. Sub-title text
5. Colored call-out box
The design must also adhere to our current brand guidelines: https://stylekit-demo.example/lantern-9
We've attached a very basic mock-up that includes the elements listed above. However, we encourage you to be more playful and/or creative with your design.
Our goal is to create a template that is flexible enough to accomodate a variety of resources (samples of 3 different resources are attached), that is also visually appealing enough to attract and hold the attention of busy educators.
Target Market(s)
Educators - Middle School, High School & College
Look and feel

```html
<!DOCTYPE html>
<html lang="en">
<head>
<meta charset="utf-8">
<title>Lantern 9 Learning Resource Template</title>
<link rel="stylesheet" href="https://fonts.googleapis.com/css2?family=Nunito+Sans:wght@400;600&family=Source+Serif+4:wght@400;500&display=swap">
<style>
  :root {
    --brand-purple: #65348f;
    --panel-blue: #eaf4fc;
    --body-ink: #333333;
    --rule-dark: #222222;
    --paper: #ffffff;
    --backdrop: #ffffff;
    --sans: "Nunito Sans", Arial, sans-serif;
    --serif: "Source Serif 4", Georgia, serif;
  }
  * { box-sizing: border-box; margin: 0; padding: 0; }
  html, body { width: 1200px; height: 1200px; overflow: hidden; background: var(--backdrop); }
  .canvas { position: relative; width: 1200px; height: 1200px; }
  .page {
    position: absolute; top: 245px; width: 524px; height: 742px;
    background: var(--paper); overflow: hidden;
    box-shadow: 0 0 6px rgba(0,0,0,0.28);
  }
  .page--one { left: 62px; }
  .page--two { left: 623px; }
  .page > * { position: absolute; }
  .top-arc { left: 0; top: 0; width: 524px; height: 120px; }
  .brand-name {
    font-family: var(--serif); font-weight: 500; color: var(--brand-purple);
    white-space: nowrap;
  }
  .page--one .brand-name { left: 51px; top: 43px; font-size: 20px; }
  .page--two .brand-name { left: 38px; top: 38px; font-size: 19px; }
  .resource-title {
    left: 71px; top: 98px; font-family: var(--serif); font-weight: 500;
    font-size: 22.5px; color: var(--brand-purple); white-space: nowrap;
  }
  .bio-panel { left: 18px; top: 207px; width: 192px; height: 375px; background: var(--panel-blue); }
  .author-photo { left: 42px; top: 146px; width: 146px; height: 146px; }
  .section-heading {
    font-family: var(--serif); font-weight: 500; color: var(--brand-purple); white-space: nowrap;
  }
  .heading-rule {
    height: 1px; background: linear-gradient(to right, var(--rule-dark) 0 30px, var(--brand-purple) 30px);
  }
  .bio-heading { left: 33px; top: 317px; font-size: 22px; }
  .bio-rule { left: 35px; top: 352px; width: 144px; }
  .bio-list { left: 33px; top: 357px; list-style: none; font-family: var(--serif); font-size: 12.3px; line-height: 17.6px; color: var(--body-ink); }
  .body-text {
    font-family: var(--sans); font-size: 10.2px; line-height: 15.85px; color: var(--body-ink); white-space: nowrap;
  }
  .intro-text { left: 224px; top: 169px; }
  .sub-heading { left: 224px; top: 380px; font-size: 16px; }
  .sub-rule { left: 224px; top: 407px; width: 275px; }
  .sub-text { left: 224px; top: 417px; }
  .callout {
    left: 48px; top: 602px; width: 435px; height: 112px; background: var(--brand-purple);
    color: #ffffff; font-family: var(--sans); white-space: nowrap;
  }
  .page--one .callout { padding: 13px 0 0 11px; font-size: 10.2px; line-height: 15.85px; }
  .page--two .callout { padding: 14px 0 0 24px; font-size: 9.8px; line-height: 12.7px; }
  .cont-heading { left: 48px; top: 89px; font-size: 17px; }
  .cont-rule { left: 48px; top: 117px; width: 442px; }
  .cont-text { left: 49px; top: 122px; }
  .next-heading { left: 39px; top: 467px; font-size: 17px; }
  .next-rule { left: 48px; top: 497px; width: 442px; background: var(--brand-purple); }
  .next-text { left: 48px; top: 502px; }
</style>
</head>
<body>
<main class="canvas">

  <section class="page page--one">
    <svg class="top-arc" viewBox="0 0 524 120" aria-hidden="true">
      <circle cx="396" cy="-33" r="97" fill="none" stroke="var(--brand-purple)" stroke-width="11"/>
    </svg>
    <div class="brand-name">Lantern 9</div>
    <h1 class="resource-title">Lorem ipsum dolor sit amet, consectetur</h1>

    <div class="bio-panel"></div>
    <svg class="author-photo" viewBox="0 0 146 146" role="img" aria-label="Author portrait photo">
      <defs>
        <radialGradient id="photoTone" cx="50%" cy="45%" r="60%">
          <stop offset="0%" stop-color="#9a9a9a"/>
          <stop offset="100%" stop-color="#4a4a4a"/>
        </radialGradient>
      </defs>
      <circle cx="73" cy="73" r="72" fill="#ffffff" stroke="var(--brand-purple)" stroke-width="1.2"/>
      <circle cx="73" cy="73" r="66" fill="url(#photoTone)"/>
    </svg>

    <h2 class="section-heading bio-heading">Writer Bio</h2>
    <div class="heading-rule bio-rule"></div>
    <ul class="bio-list">
      <li>Lorem ipsum dolor sit amet</li>
      <li>Lorem ipsum dolor sit amet</li>
      <li>Lorem ipsum dolor sit amet</li>
      <li>Lorem ipsum dolor sit amet</li>
      <li>Lorem ipsum dolor sit amet</li>
      <li>Lorem ipsum dolor sit amet</li>
    </ul>

    <p class="body-text intro-text">Lorem ipsum dolor sit amet, consectetur adipiscing<br>elit. Morbi ut libero mattis, pellentesque urna eu, iacu-<br>lis lorem. Interdum et malesuada fames ac ante ipsum<br>primis in faucibus. Duis pellen- tesque orci consecte-<br>tur sapien vulputate imperdiet. Aliquam erat volutpat.<br>Integer tristique erat lorem, sed posuere enim rhoncus<br>sed. Fusce ut venenatis nulla, sed elementum arcu.<br>Maecenas eu- ismod mauris euismod augue posuere<br>venenatis. Duis id porta ante integer.</p>

    <h2 class="section-heading sub-heading">Sub-header Text - Lorem ipsum dolor sit</h2>
    <div class="heading-rule sub-rule"></div>
    <p class="body-text sub-text">Lorem ipsum dolor sit amet, consectetur adipiscing<br>elit. Morbi ut libero mattis, pellentesque urna eu, iacu-<br>lis lorem. Interdum et malesuada fames ac ante ipsum<br>primis in faucibus. Duis pellen- tesque orci consecte-<br>tur sapien vulputate imperdiet. Aliquam erat volutpat.<br>Integer tristique erat lorem, sed posuere enim rhoncus<br>sed. Fusce ut venenatis nulla, sed elementum arcu.<br>Maecenas eu- ismod mauris euismod augue posuere<br>venenatis. Duis id porta ante integer.</p>

    <aside class="callout">Lorem ipsum dolor sit amet, consectetur adipiscing elit. Morbi ut libero mattis, pellen-<br>tesque urna eu, iaculis lorem. Interdum et malesuada fames ac ante ipsum primis in fauci-<br>bus. Duis pellen- tesque orci consectetur sapien vulputate imperdiet. Aliquam erat volut-<br>pat. Integer tristique erat lorem, sed posuere enim rhoncus sed. Fusce ut venenatis nulla,<br>sed elementum arcu. Maecenas eu- ismod mauris euismod augue posuere venenatis.</aside>
  </section>

  <section class="page page--two">
    <svg class="top-arc" viewBox="0 0 524 120" aria-hidden="true">
      <circle cx="411" cy="-14" r="72" fill="none" stroke="var(--brand-purple)" stroke-width="11"/>
    </svg>
    <div class="brand-name">Lantern 9</div>

    <h2 class="section-heading cont-heading">Lorem ipsum dolor sit (cont’d)</h2>
    <div class="heading-rule cont-rule"></div>
    <p class="body-text cont-text">Lorem ipsum dolor sit amet, consectetur adipiscing elit. Morbi ut libero mattis, pellentesque<br>urna eu, iaculis lorem. Interdum et malesuada fames ac ante ipsum primis in faucibus. Duis<br>pellen- tesque orci consectetur sapien vulputate imperdiet. Aliquam erat volutpat. Integer tris-<br>tique erat lorem, sed posuere enim rhoncus sed. Fusce ut venenatis nulla, sed elementum arcu.<br>Maecenas eu- ismod mauris euismod augue posuere venenatis. Duis id porta ante integer.<br>Lorem ipsum dolor sit amet, consectetur adipiscing elit. Morbi ut libero mattis, pellentesque<br>urna eu, iaculis lorem. Interdum et malesuada fames ac ante ipsum primis in faucibus. Duis<br>pellen- tesque orci consectetur sapien vulputate imperdiet. Aliquam erat volutpat. Integer tris-<br>tique erat lorem, sed posuere enim rhoncus sed. Fusce ut venenatis nulla, sed elementum arcu.<br>Maecenas eu- ismod mauris euismod augue posuere venenatis. Duis id porta ante integer.<br>Lorem ipsum dolor sit amet, consectetur adipiscing elit. Morbi ut libero mattis, pellentesque<br>urna eu, iaculis lorem. Interdum et malesuada fames ac ante ipsum primis in faucibus. Duis<br>pellen- tesque orci consectetur sapien vulputate imperdiet. Aliquam erat volutpat. Integer tris-<br>tique erat lorem, sed posuere enim rhoncus sed. Fusce ut venenatis nulla, sed elementum arcu.<br>Maecenas eu- ismod mauris euismod augue posuere venenatis. Duis id porta ante integer.<br>Lorem ipsum dolor sit amet, consectetur adipiscing elit. Morbi ut libero mattis, pellentesque<br>urna eu, iaculis lorem. Interdum et malesuada fames ac ante ipsum primis in faucibus. Duis<br>pellen- tesque orci consectetur sapien vulputate imperdiet. Aliquam erat volutpat. Integer tris-<br>tique erat lorem, sed posuere enim rhoncus sed. Fusce ut venenatis nulla, sed elementum arcu.<br>Maecenas eu- ismod mauris euismod augue posuere venenatis. Duis id porta ante integer.</p>

    <h2 class="section-heading next-heading">- Lorem ipsum dolor sit</h2>
    <div class="heading-rule next-rule"></div>
    <p class="body-text next-text">Lorem ipsum dolor sit amet, consectetur adipiscing elit. Morbi ut libero mattis, pellentesque<br>urna eu, iaculis lorem. Interdum et malesuada fames ac ante ipsum primis in faucibus. Duis<br>pellen- tesque orci consectetur sapien vulputate imperdiet. Aliquam erat volutpat. Integer tris-<br>tique erat lorem, sed posuere enim rhoncus sed. Fusce ut venenatis nulla, sed elementum arcu.<br>Maecenas eu- ismod mauris euismod augue posuere venenatis. Duis id porta ante integer.</p>

    <aside class="callout">Lorem ipsum dolor sit amet, consectetur adipiscing elit. Morbi ut libero mattis,<br>pellentesque urna eu, iaculis lorem. Interdum et malesuada fames ac ante ipsum<br>primis in faucibus. Duis pellen- tesque orci consectetur sapien vulputate imperdi-<br>et. Aliquam erat volutpat. Integer tristique erat lorem, sed posuere enim rhoncus<br>sed. Fusce ut venenatis nulla, sed elementum arcu. Maecenas eu- ismod mauris<br>euismod augue posuere venenatis. Duis id porta ante integer.</aside>
  </section>

</main>
</body>
</html>
```